'Ormel Property Development' Business Card

Business Card Features:

High Quality (potentially textured) thick card - preference is white textured card

Logo (supplied)

We plan to use the vertical logo as the main logo. But i am happy for people to use either if they find it works better for the design of the card.

The building icon and also the insert to the 'E' is in a metallic finish, i think this should be finished in a metallic embossed or raised style.
Updates

Please note i have attached both a horizontal and Vertical Logo for your reference. We plan to use the vertical logo as the main logo. But i am happy for people to use either if they find it works better for the design of the card.

Please note i am considering having the cards made on stainless steel. This introduces the option of having cut outs in the card and etching or printing for the design. If you have a good concept for this please submit.

http://www.tinquarry.example/black-metal-cards# this is a site that makes the metal cards to offer some direction . . . . Please note i am basic the selection o the best design, if that means normal print cards on paper then this is what i will choose. But there are some great options with the metal. Thanks.

Industry/Entity Type

Building

Requirements
Must have
• Helvetica font to details side of card - logo as supplied to opposite side.

Card Details:

Darrow Pketts
Managing Director

+61 487 263 518
+61 3 6172 4809

PO Box 73
Bentleigh, VIC 3024

darrow@ormel.example

www.ormel.example

```html
<!DOCTYPE html>
<html lang="en">
<head>
<meta charset="utf-8">
<title>Ormel Property Development – Business Card</title>
<link rel="stylesheet" href="https://fonts.googleapis.com/css2?family=Arimo:wght@400;700&display=swap">
<style>
  :root {
    --backdrop: #cfc9c3;
    --card-top: #f1f0ef;
    --card-bottom: #dcdad8;
    --ink-dark: #3b3d40;
    --ink-mid: #5c5e61;
    --ink-soft: #7d7f82;
    --rule: #4a4c4f;
    --band-light: rgba(120,121,124,0);
    --band-mid: #8a8b8e;
    --band-dark: #3a3b3e;
  }
  html, body {
    margin: 0;
    width: 1200px;
    height: 970px;
    overflow: hidden;
    background: var(--backdrop);
    font-family: "Arimo", "Helvetica Neue", Helvetica, Arial, sans-serif;
  }
  .card {
    position: absolute;
    left: 100px;
    top: 207px;
    width: 1000px;
    height: 556px;
    background: linear-gradient(180deg, var(--card-top), var(--card-bottom));
    box-shadow: 0 10px 30px rgba(0,0,0,0.18);
    overflow: hidden;
  }
  .brand {
    position: absolute;
    left: 57px;
    top: 52px;
    display: flex;
    align-items: center;
    gap: 22px;
    color: var(--ink-mid);
    font-weight: 700;
  }
  .brand-square {
    width: 56px;
    height: 56px;
    background: var(--ink-mid);
  }
  .brand-name {
    font-size: 62px;
    line-height: 1;
    letter-spacing: 2px;
  }
  .brand-tag {
    font-size: 16px;
    letter-spacing: 1px;
    margin-top: 8px;
  }
  .person {
    position: absolute;
    right: 49px;
    top: 210px;
    text-align: right;
  }
  .person-name {
    font-size: 28px;
    font-weight: 700;
    color: var(--ink-dark);
  }
  .person-role {
    font-size: 21px;
    color: var(--ink-soft);
    margin-top: 4px;
  }
  .divider {
    position: absolute;
    left: 50px;
    right: 53px;
    top: 305px;
    height: 2px;
    background: var(--rule);
  }
  .address {
    position: absolute;
    left: 50px;
    top: 330px;
    font-size: 21px;
    line-height: 29px;
    color: var(--ink-soft);
  }
  .contacts {
    position: absolute;
    right: 44px;
    top: 330px;
    list-style: none;
    margin: 0;
    padding: 0;
    font-size: 21px;
    line-height: 29px;
    color: var(--ink-mid);
    text-align: right;
  }
  .contacts li {
    display: flex;
    justify-content: flex-end;
    align-items: center;
    gap: 12px;
  }
  .contacts svg { width: 22px; height: 22px; fill: var(--ink-dark); }
  .footer-band {
    position: absolute;
    left: 0;
    right: 0;
    bottom: 0;
    height: 104px;
    background: linear-gradient(180deg, var(--band-light) 0%, var(--band-mid) 45%, var(--band-dark) 100%);
  }
</style>
</head>
<body>
  <div class="card">
    <div class="brand">
      <div class="brand-square"></div>
      <div>
        <div class="brand-name">ORMEL</div>
        <div class="brand-tag">PROPERTY DEVELOPMENT</div>
      </div>
    </div>

    <div class="person">
      <div class="person-name">Darrow Pketts</div>
      <div class="person-role">Managing Director</div>
    </div>

    <div class="divider"></div>

    <div class="address">PO Box 73 Bentleigh,<br>VIC 3024</div>

    <ul class="contacts">
      <li>+61 487 263 518
        <svg viewBox="0 0 24 24"><path d="M3 9c0-3 4-5 9-5s9 2 9 5v2h-5V9H8v2H3z M6 12h12l2 8H4z M12 14a2.5 2.5 0 1 0 0 5a2.5 2.5 0 1 0 0-5z"/></svg>
      </li>
      <li>+61 3 6172 4809
        <svg viewBox="0 0 24 24"><path d="M7 2h10a1 1 0 0 1 1 1v18a1 1 0 0 1-1 1H7a1 1 0 0 1-1-1V3a1 1 0 0 1 1-1zm1 3v12h8V5zm4 13.5a1 1 0 1 0 0 2a1 1 0 1 0 0-2z"/></svg>
      </li>
      <li>darrow@ormel.example
        <svg viewBox="0 0 24 24"><path d="M2 5h20v14H2zm2 2v.5l8 5 8-5V7zm0 3v7h16v-7l-8 5z"/></svg>
      </li>
      <li>www.ormel.example
        <svg viewBox="0 0 24 24"><path d="M2 4h20v13H2zm2 2v9h16V6zm5 13h6v2H9z"/></svg>
      </li>
    </ul>

    <div class="footer-band" role="img" aria-label="Decorative grey and charcoal flowing bands along the bottom edge of the card"></div>
  </div>
</body>
</html>
```